Wine Label for a wine from Tuscany, Italy

We need a wine label for a white and red wine, can be the same label or can be somewhat differentiated with any variation you feel would be good.. These two wines come from Tuscany, Italy. Wine labels from Tuscany Italy tend to be traditional. We are open to traditional looking labels but also more modern, eye catching too. We want to convey a sense of elegance, importance, great wine. I am attaching some examples of labels we like from Tuscany, also a label that was designed for us recently by one of you, which we LOVE. No wine glasses, wine bottles or grapes featured on the label please. We tend to like the white background. No blue please.

Target Market(s)

More women than men purchase wine, but it needs to appeal to both sexes.

Requirements
Must have
• Wine Name: Corte L' or Corte l'
• Type/Varletal: Rosso Toscano (White is Vermentino)
• Vintage (year): 2018
• That is all the text we want on the label, thanks
Nice to have
• Clean, something that makes someone want to grab this wine bottle off the shelf!
Should not have
• Images of Wine glass, wine bottles, grapes
• Do not use the color blue please.

```html
<!DOCTYPE html>
<html lang="it">
<head>
<meta charset="utf-8">
<title>Corte L' — Vermentino Toscano 2018</title>
<link rel="stylesheet" href="https://fonts.googleapis.com/css2?family=Great+Vibes&family=Bodoni+Moda:wght@600;700&display=swap">
<style>
  :root {
    --backdrop: #1b1f24;
    --paper: #f3f0e8;
    --paper-shade: #e6e1d4;
    --gold: #c9a227;
    --gold-light: #e8cf6a;
    --silver: #8e9298;
    --ink-grey: #5d6066;
  }
  * { margin: 0; padding: 0; box-sizing: border-box; }
  html, body {
    width: 1200px;
    height: 860px;
    overflow: hidden;
    background: var(--backdrop);
  }
  .canvas {
    position: relative;
    width: 1200px;
    height: 860px;
    display: flex;
    align-items: center;
    justify-content: center;
  }
  .wine-label {
    position: relative;
    width: 760px;
    height: 640px;
    background: linear-gradient(180deg, var(--paper) 0%, var(--paper) 70%, var(--paper-shade) 100%);
    overflow: hidden;
  }
  .label-rule-top {
    position: absolute;
    top: 14px; left: 0; right: 0;
    height: 4px;
    background: linear-gradient(90deg, var(--gold), var(--gold-light), var(--gold));
  }
  .label-band-bottom {
    position: absolute;
    bottom: 0; left: 0; right: 0;
    height: 34px;
    background: linear-gradient(90deg, var(--gold), var(--gold-light), var(--gold));
  }
  .label-curve {
    position: absolute;
    inset: 0;
    width: 100%;
    height: 100%;
  }
  .wine-name {
    position: absolute;
    top: 96px;
    left: 0; right: 0;
    text-align: center;
    font-family: "Great Vibes", cursive;
    font-size: 168px;
    line-height: 1;
    color: var(--gold);
  }
  .wine-details {
    position: absolute;
    top: 390px;
    left: 0; right: 0;
    text-align: center;
    font-family: "Bodoni Moda", serif;
    font-weight: 700;
    line-height: 1.05;
  }
  .varietal {
    font-size: 54px;
    letter-spacing: 1px;
    color: var(--silver);
  }
  .region {
    font-size: 34px;
    letter-spacing: 2px;
    color: var(--ink-grey);
  }
  .vintage {
    margin-top: 6px;
    font-size: 38px;
    letter-spacing: 2px;
    color: var(--gold);
  }
</style>
</head>
<body>
  <main class="canvas">
    <section class="wine-label">
      <div class="label-rule-top"></div>
      <svg class="label-curve" viewBox="0 0 760 640" aria-hidden="true">
        <path d="M 40 640 C 60 420, 200 300, 360 300 C 520 300, 640 260, 720 180"
              fill="none" stroke="#c9a227" stroke-width="3"/>
      </svg>
      <h1 class="wine-name">Corte L'</h1>
      <div class="wine-details">
        <p class="varietal">VERMENTINO</p>
        <p class="region">TOSCANO</p>
        <p class="vintage">2018</p>
      </div>
      <div class="label-band-bottom"></div>
    </section>
  </main>
</body>
</html>
```